Primary School
Website for a Primary School
Education
http://sp7.wierzbowe-lato.pl/
The full name of the school is:
Szkoła Podstawowa nr 7 im. Bolesława Czerniaka w Lipowej Dolinie.
The name must be placed somewhere at the top of the website
The school is a primary (elementary) school in Poland, in a town of Lipowa Dolina. The pupils are children 6-11 years old (there are 6 grades).
The website will contain: news, events, timetable (lesson plan), pictures of class/school events. Generally, there will be many photos on the website.
The website should include the current date and name day information in Polish: "Dzisiaj jest wtorek, 30 listopada, imieniny Andrzeja, Justyny" (English translation is: "Today is Tuesday, 30 November, name day of Andrzej, Justyna", but please use Polish version in your drafts).
And also weather forecast for Lipowa Dolina information should be embedded in the website.
The website should be modern and at the same time clear, friendly and nice with a simple, intuitive navigation.
We like websites that are user-friendly and nice.
A site-map at the bottom would be nice.
The navigation should be top but the submenus might appear on the left.
Elegant
blue/navy (the colors of the logo)
Logo
Website/Menu Structure

```html
<!DOCTYPE html>
<html lang="pl">
<head>
<meta charset="utf-8">
<title>Szkoła Podstawowa nr 7 im. Bolesława Czerniaka w Lipowej Dolinie</title>
<link href="https://fonts.googleapis.com/css2?family=Open+Sans:ital,wght@0,400;0,600;0,700;1,400&family=PT+Serif:ital@1&family=Arimo:wght@400;700&display=swap" rel="stylesheet">
<style>
:root{
  --paper:#f4f1ea;
  --paper-line:#ebe6dc;
  --red:#c8181e;
  --red-active:#6f0a0d;
  --navy:#1f3a66;
  --ink:#3b3b3b;
  --muted:#7a7a7a;
  --panel-dark:#3a3f45;
  --panel-dark2:#2b2f34;
  --link-red:#d42b2b;
  --sky-top:#2f8fd8;
  --sky-bottom:#bfe3f7;
  --grass:#5fae2a;
  --grass-light:#a6d86a;
  --white:#ffffff;
}
*{box-sizing:border-box;margin:0;padding:0}
html,body{width:1200px;height:1096px;overflow:hidden}
body{
  position:relative;
  background:repeating-linear-gradient(90deg,var(--paper) 0 6px,var(--paper-line) 6px 7px);
  font-family:'Arimo',Arial,sans-serif;color:var(--ink);font-size:11px;line-height:1.45;
}
.abs{position:absolute}

/* header */
.brand{left:262px;top:30px;width:100px;height:120px;display:flex;flex-direction:column;align-items:center;justify-content:center;gap:10px}
.brand-mark{width:70px;height:70px;border-radius:50%;background:var(--navy)}
.brand-name{font-family:'Open Sans',sans-serif;font-weight:700;font-size:15px;color:var(--navy)}
.today{left:380px;top:56px;width:270px;text-align:center;font-family:'PT Serif',serif;font-style:italic;font-size:13px;color:#444;line-height:1.4}
.weather{left:660px;top:30px;width:300px}
.weather-title{position:absolute;left:40px;top:0;font-weight:700;font-size:11px;color:#555;white-space:nowrap}
.weather-icon{position:absolute;left:0;top:28px;width:95px;height:70px;border-radius:35px;background:radial-gradient(circle at 30% 35%,#ffd23f 0 28%,transparent 30%),linear-gradient(#fafafa,#c9d3dc)}
.weather-temp{position:absolute;left:120px;top:32px;font-family:'Open Sans',sans-serif;font-size:18px;font-weight:600;color:#444}
.weather-info{position:absolute;left:112px;top:66px;font-size:9px;color:var(--muted);line-height:1.35}

/* main menu */
.main-nav{left:255px;top:178px;width:165px;background:linear-gradient(90deg,var(--red),#a81216);padding:8px 0;box-shadow:0 2px 4px rgba(0,0,0,.25)}
.main-nav a{display:block;height:34px;line-height:34px;padding-left:22px;color:var(--white);text-decoration:none;font-family:'Open Sans',sans-serif;font-size:13px;position:relative}
.main-nav a::before{content:"";position:absolute;left:10px;top:14px;border:4px solid transparent;border-left:5px solid var(--white)}
.main-nav a.is-active{background:var(--red-active)}

/* slider */
.hero{left:435px;top:172px;width:525px;height:248px;background:var(--white);padding:8px;border-radius:6px;box-shadow:0 1px 4px rgba(0,0,0,.25)}
.hero-photo{width:100%;height:100%;border-radius:4px;background:linear-gradient(var(--sky-top),var(--sky-bottom) 75%,#e9dcc4);position:relative;overflow:hidden}
.hero-title{position:absolute;left:48px;top:60px;font-family:'Open Sans',sans-serif;font-weight:700;font-size:27px;color:var(--white);line-height:1.2}
.hero-more{position:absolute;left:48px;top:132px;font-size:10px;color:#e8f6ff}
.hero-dots{position:absolute;left:0;right:0;bottom:0;height:26px;background:#e9e9e9;display:flex;justify-content:center;align-items:center;gap:8px}
.hero-dots span{width:8px;height:8px;border-radius:50%;background:#aaa}
.hero-dots span.is-current{background:var(--red)}

/* news sidebar */
.news{left:255px;top:425px;width:165px;background:var(--white);padding:12px;border:1px solid #e2ddd3}
.news h3{color:var(--red);font-size:11px;font-weight:700;padding-bottom:6px;border-bottom:1px solid #ddd;margin-bottom:10px}
.news-item{display:flex;gap:7px;margin-bottom:12px}
.news-icon{flex:none;width:14px;height:14px;background:var(--red);border-radius:2px;margin-top:2px}
.news-item h4{font-size:10.5px;font-weight:700;color:#333}
.news-item p{font-size:9px;color:var(--muted);line-height:1.35}

/* welcome */
.welcome{left:452px;top:430px;width:505px}
.welcome h1{font-family:'Open Sans',sans-serif;font-size:14px;font-weight:400;color:#333}
.welcome h2{font-family:'Open Sans',sans-serif;font-size:14px;font-weight:700;color:var(--red);margin-bottom:14px}
.welcome p{font-size:9.5px;color:var(--muted);margin-bottom:10px;line-height:1.45}

/* lower panels */
.panel-head{height:34px;background:linear-gradient(var(--panel-dark),var(--panel-dark2));color:var(--white);font-family:'Open Sans',sans-serif;font-size:12px;display:flex;align-items:center;gap:8px;padding-left:10px}
.panel-head i{width:14px;height:12px;border-radius:2px;background:#6cb4e8;display:block}
.panel-head i.is-gallery{background:#e8e8e8}
.schedule{left:255px;top:640px;width:165px;height:160px;background:var(--white)}
.schedule ul{list-style:none;padding:10px 12px;font-size:9.5px;color:#555;line-height:1.5}
.more{position:absolute;right:10px;bottom:8px;color:var(--link-red);font-size:9px}
.gallery{left:450px;top:640px;width:510px;height:160px;background:var(--white)}
.gallery-row{display:flex;gap:12px;padding:14px 12px 0}
.thumb{flex:1;height:72px;border:3px solid var(--white);box-shadow:0 0 0 1px #ddd}
.thumb-a{background:linear-gradient(135deg,#8fb7d6,#e0c7a3)}
.thumb-b{background:linear-gradient(135deg,#f0c66b,#6ea6d8)}
.thumb-c{background:linear-gradient(135deg,#d6b08a,#7fb36a)}
.thumb-d{background:linear-gradient(135deg,#9fc4e6,#e9d9c2)}

/* footer */
.footer-col h5{font-family:'Open Sans',sans-serif;font-size:12px;font-weight:700;color:var(--red);margin-bottom:10px}
.footer-col{font-size:9.5px;color:#555;line-height:1.7}
.sitemap{left:258px;top:815px;width:170px}
.sitemap .cols{display:flex;gap:32px}
.sitemap a{color:#555;text-decoration:none;display:block}
.contact{left:452px;top:815px;width:370px}
.contact dl{display:grid;grid-template-columns:44px 110px 48px 1fr;column-gap:8px;white-space:nowrap}
.contact dd{color:#555}
.contact dt{color:#333}
.social{left:830px;top:815px;width:130px}
.social .badges{display:flex;gap:10px}
.social .badges span{width:30px;height:30px;border-radius:50%;background:#3b6fb6}
.social .badges span:nth-child(2){background:#3ea9e0}
.social .badges span:nth-child(3){background:#2b7bb9}
.rule{left:255px;top:955px;width:705px;border-top:1px dotted #bbb}
.copyright{left:255px;top:963px;width:705px;text-align:center;font-size:8.5px;color:var(--muted)}
.grass{left:0;top:1000px;width:1200px;height:96px;background:linear-gradient(transparent,var(--grass-light) 35%,var(--grass))}
</style>
</head>
<body>

<header>
  <div class="abs brand">
    <span class="brand-mark"></span>
    <span class="brand-name">SP nr 7</span>
  </div>
  <p class="abs today">"Dzisiaj jest wtorek, 30 listopada,<br>imieniny Andrzeja, Justyny"</p>
  <section class="abs weather" aria-label="Pogoda">
    <p class="weather-title">Pogoda Lipowa Dolina, Polska</p>
    <div class="weather-icon" role="img" aria-label="Ikona pogody: słońce za chmurą"></div>
    <p class="weather-temp">1°C | °F</p>
    <p class="weather-info">Częściowe zachmurzenie<br>Wiatr: płd.-zach. 10 km/h<br>Wilgotność: 81%</p>
  </section>
</header>

<nav class="abs main-nav">
  <a href="#">Strona główna</a>
  <a href="#" class="is-active">Aktualności</a>
  <a href="#">Szkoła</a>
  <a href="#">Galeria</a>
  <a href="#">Sport</a>
  <a href="#">Kontakt</a>
</nav>

<section class="abs hero">
  <div class="hero-photo" role="img" aria-label="Zdjęcie: dziecko bawiące się samolotem na tle nieba">
    <p class="hero-title">Idealne miejsce<br>dla dzieci</p>
    <p class="hero-more">Więcej informacji »</p>
    <div class="hero-dots"><span class="is-current"></span><span></span><span></span><span></span></div>
  </div>
</section>

<aside class="abs news">
  <h3>Aktualności i wydarzenia</h3>
  <article class="news-item">
    <span class="news-icon"></span>
    <div><h4>Lorem ipsum dolor sit</h4><p>Lorem ipsum dolor sit amet, consectetur adipiscing elit.</p></div>
  </article>
  <article class="news-item">
    <span class="news-icon"></span>
    <div><h4>Lorem ipsum dolor sit</h4><p>Lorem ipsum dolor sit amet, consectetur adipiscing elit.</p></div>
  </article>
</aside>

<main class="abs welcome">
  <h1>Witamy</h1>
  <h2>Szkoła Podstawowa nr 7 im. Bolesława Czerniaka w Lipowej Dolinie</h2>
  <p>Tymczasowy tekst przyjdzie tutaj. Tymczasowy tekst przyjdzie tutaj. Tymczasowy tekst przyjdzie tutaj. Tymczasowy tekst przyjdzie tutaj. Tymczasowy tekst przyjdzie tutaj. Tymczasowy tekst przyjdzie tutaj.</p>
  <p>Tymczasowy tekst przyjdzie tutaj. Tymczasowy tekst przyjdzie tutaj. Tymczasowy tekst przyjdzie tutaj. Tymczasowy tekst przyjdzie tutaj. Tymczasowy tekst przyjdzie tutaj. Tymczasowy tekst przyjdzie tutaj. Tymczasowy tekst przyjdzie tutaj. Tymczasowy tekst przyjdzie tutaj.</p>
  <p>Tymczasowy tekst przyjdzie tutaj. Tymczasowy tekst przyjdzie tutaj. Tymczasowy tekst przyjdzie tutaj. Tymczasowy tekst przyjdzie tutaj. Tymczasowy tekst przyjdzie tutaj. Tymczasowy tekst przyjdzie tutaj. Tymczasowy tekst przyjdzie tutaj.</p>
</main>

<section class="abs schedule">
  <div class="panel-head"><i></i>Rozkład</div>
  <ul>
    <li>Tymczasowy tekst przyjdzie tutaj</li>
    <li>Tymczasowy tekst przyjdzie tutaj</li>
    <li>Tymczasowy tekst przyjdzie tutaj</li>
    <li>Tymczasowy tekst przyjdzie tutaj</li>
    <li>Tymczasowy tekst przyjdzie tutaj</li>
  </ul>
  <a class="more">Zobacz więcej</a>
</section>

<section class="abs gallery">
  <div class="panel-head"><i class="is-gallery"></i>Galeria zdjęć</div>
  <div class="gallery-row">
    <div class="thumb thumb-a" role="img" aria-label="Zdjęcie z życia szkoły: uczniowie w klasie"></div>
    <div class="thumb thumb-b" role="img" aria-label="Zdjęcie z życia szkoły: dzieci na zajęciach"></div>
    <div class="thumb thumb-c" role="img" aria-label="Zdjęcie z życia szkoły: uczniowie przy ławkach"></div>
    <div class="thumb thumb-d" role="img" aria-label="Zdjęcie z życia szkoły: dzieci podczas wydarzenia"></div>
  </div>
  <a class="more">Zobacz więcej</a>
</section>

<footer>
  <nav class="abs footer-col sitemap">
    <h5>nawigacja</h5>
    <div class="cols">
      <div><a>Strona główna</a><a>Aktualności</a><a>Szkoła</a><a>Galeria</a></div>
      <div><a>Sport</a><a>Kontakt</a></div>
    </div>
  </nav>
  <section class="abs footer-col contact">
    <h5>Kontakt z nami</h5>
    <dl>
      <dt>Adres:</dt><dd>ul. Klonowa 14</dd><dt>Telefon:</dt><dd>61 812 34 56</dd>
      <dt></dt><dd>12-345 Lipowa</dd><dt>Fax:</dt><dd>61 812 34 57</dd>
      <dt></dt><dd>Dolina</dd><dt>E-mail:</dt><dd>sekretariat@wierzbowe-lato.pl</dd>
    </dl>
  </section>
  <section class="abs footer-col social">
    <h5>Dołącz do nas</h5>
    <div class="badges"><span></span><span></span><span></span></div>
  </section>
  <div class="abs rule"></div>
  <p class="abs copyright">prawa autorskie © 2011, Szkoła Podstawowa nr 7 im. Bolesława Czerniaka w Lipowej Dolinie. Wszelkie prawa zastrzeżone.</p>
  <div class="abs grass" role="img" aria-label="Ilustracja: trawa z kwiatami na dole strony"></div>
</footer>

</body>
</html>
```